Pemby Skatewear Brochure

tagline_
- skatewear for everywhere

Brochure to showcase our clothing line/products
Sending to various stores around the country for them to carry the line.
Fun, attention getting brochure.
Template that we can change per season for different clothing/new products.
I've included my logo and can provide all photo's of current clothing that will need to be included in the brochure.

PLEASE USE IMAGE IMG_1454.JPG FOR COVER OF BROCHURE

Target Market(s)

Figure Skaters around the world. Age range anywhere between 4yrs old to an adult skater. Ice Skaters and fan's of ice skating. Female

Industry/Entity Type

Clothing

Requirements
Must have
• All photo's of clothing products/ descriptions

Must have product description next to each photo.
Glitter Comet etc.

Mission statement:
At Pemby our goal is to provide you cutting edge, super stylish, high quality apparel that’s wearable on the ice or out on the town.

Contact information for Brochure.

Contact us at:
Pemby Skatewear
PO Box 4738
Sun Valley, Idaho 83519
Phone: 208-555-0147
Email: info@pembyskatewear-example.com
www.pembyskatewear-example.com
www.facebook.com/pembyskatewearexample
www.twitter.com/pembyskatewearexample

```html
<!DOCTYPE html>
<html lang="en">
<head>
<meta charset="utf-8">
<title>Pemby Skatewear Brochure</title>
<link href="https://fonts.googleapis.com/css2?family=Open+Sans:wght@400;600&family=Satisfy&display=swap" rel="stylesheet">
<style>
  :root {
    --pink: #ee3a80;
    --pink-deep: #d9266c;
    --grey-text: #6d6d6d;
    --grey-mark: #a7a9ac;
    --white: #ffffff;
    --price-ink: #333333;
    --price-edge: #b9b9b9;
  }
  * { margin: 0; padding: 0; box-sizing: border-box; }
  html, body { width: 1200px; height: 900px; overflow: hidden; background: var(--white); }
  body { position: relative; font-family: "Open Sans", Arial, sans-serif; }

  .page {
    position: absolute;
    width: 473px;
    height: 670px;
    background: var(--white);
    border: 1px solid var(--pink);
    box-shadow: 2px 3px 5px rgba(0,0,0,0.25);
    overflow: hidden;
  }
  .page--cover { left: 87px; top: 50px; }
  .page--collection { left: 630px; top: 192px; }
  .page-art { position: absolute; left: 0; top: 0; width: 473px; height: 670px; }

  .brand {
    position: absolute;
    display: flex;
    align-items: center;
    gap: 8px;
    font-weight: 600;
    color: var(--pink);
    z-index: 2;
  }
  .brand-dot { border-radius: 50%; background: var(--grey-mark); }
  .page--cover .brand { left: 10px; top: 60px; font-size: 24px; }
  .page--cover .brand-dot { width: 26px; height: 26px; }
  .page--collection .brand { left: 18px; top: 14px; font-size: 18px; }
  .page--collection .brand-dot { width: 20px; height: 20px; }

  .tagline {
    position: absolute;
    right: 11px;
    font-family: "Satisfy", cursive;
    font-size: 26px;
    color: var(--pink);
    white-space: nowrap;
  }
  .page--cover .tagline { top: 22px; }
  .page--collection .tagline { top: 8px; }

  .mission {
    position: absolute;
    right: 11px;
    width: 245px;
    text-align: right;
    font-size: 12.5px;
    line-height: 16px;
    color: var(--grey-text);
  }
  .page--cover .mission { top: 66px; }
  .page--collection .mission { top: 48px; }

  .contact {
    position: absolute;
    left: 0; right: 0;
    text-align: center;
    font-size: 11px;
    line-height: 14px;
    color: var(--white);
    font-style: normal;
  }
  .contact-line { display: block; white-space: nowrap; }
  .contact-line--long { font-size: 8.8px; }
  .page--cover .contact { top: 623px; }
  .page--collection .contact { top: 652px; }
  .sep { margin: 0 5px; }

  .season-title {
    position: absolute;
    left: 56px;
    top: 82px;
    font-family: "Satisfy", cursive;
    font-size: 42px;
    font-weight: 400;
    color: var(--white);
  }
  .season-sub {
    position: absolute;
    left: 92px;
    top: 130px;
    font-family: "Satisfy", cursive;
    font-size: 21px;
    color: var(--white);
  }

  .product { position: absolute; left: 177px; width: 280px; color: var(--white); font-size: 9.5px; line-height: 12.5px; }
  .product-name { text-transform: uppercase; }
  .product--one { top: 196px; }
  .product--two { top: 333px; }
  .product--three { top: 514px; }

  .price {
    position: absolute;
    left: 342px;
    width: 87px;
    height: 24px;
    border: 1px solid var(--price-edge);
    border-radius: 4px;
    background: var(--white);
    color: var(--price-ink);
    font-size: 11.5px;
    line-height: 22px;
    text-align: center;
    white-space: nowrap;
    box-shadow: 0 1px 2px rgba(0,0,0,0.2);
  }
  .price--one { top: 258px; }
  .price--two { top: 395px; }
  .price--three { top: 576px; }
</style>
</head>
<body>

<section class="page page--cover">
  <svg class="page-art" viewBox="0 0 473 670" xmlns="http://www.w3.org/2000/svg">
    <defs>
      <linearGradient id="cover-photo-tone" x1="0" y1="0" x2="1" y2="1">
        <stop offset="0" stop-color="#3b4a5e"/>
        <stop offset="0.45" stop-color="#c79a7e"/>
        <stop offset="1" stop-color="#27303f"/>
      </linearGradient>
      <linearGradient id="cover-skater-tone" x1="0" y1="0" x2="1" y2="1">
        <stop offset="0" stop-color="#7a3fa0"/>
        <stop offset="0.5" stop-color="#e0337a"/>
        <stop offset="1" stop-color="#35a9e0"/>
      </linearGradient>
      <path id="heart" d="M50,90 C20,70 0,50 0,28 C0,10 14,0 28,0 C40,0 48,8 50,18 C52,8 60,0 72,0 C86,0 100,10 100,28 C100,50 80,70 50,90 Z"/>
    </defs>
    <path class="cover-band" fill="var(--pink)" d="M0,290 C10,190 90,140 160,145 C210,148 240,190 250,245 C280,220 340,210 400,225 C440,235 473,270 473,330 L473,670 L0,670 Z"/>
    <g role="img" aria-label="Cover photo of a smiling young skater with long hair in a dark top">
      <use href="#heart" transform="translate(28,200) scale(3.9) rotate(-12,50,45)" fill="url(#cover-photo-tone)" stroke="var(--white)" stroke-width="4"/>
    </g>
    <g role="img" aria-label="Illustration of a figure skater in a pink dress">
      <use href="#heart" transform="translate(223,395) scale(1.9) rotate(10,50,45)" fill="none" stroke="var(--grey-mark)" stroke-width="9"/>
      <use href="#heart" transform="translate(223,395) scale(1.9) rotate(10,50,45)" fill="url(#cover-skater-tone)" stroke="var(--white)" stroke-width="5"/>
    </g>
  </svg>

  <div class="brand"><span class="brand-dot"></span>Pemby</div>
  <p class="tagline">skatewear for everywhere</p>
  <p class="mission">At Pemby our goal is to provide you cutting edge, super stylish, high quality apparel that’s wearable on the ice or out on the town.</p>

  <address class="contact">
    <span class="contact-line">PEMBY SKATEWEAR</span>
    <span class="contact-line">PO Box 4738, Sun Valley, Idaho 83519</span>
    <span class="contact-line contact-line--long">Phone: 208-555-0147<span class="sep">|</span>Email: info@pembyskatewear-example.com<span class="sep">|</span>www.pembyskatewear-example.com</span>
  </address>
</section>

<section class="page page--collection">
  <svg class="page-art" viewBox="0 0 473 670" xmlns="http://www.w3.org/2000/svg">
    <defs>
      <linearGradient id="product-photo-tone" x1="0" y1="0" x2="1" y2="1">
        <stop offset="0" stop-color="#3b4a5e"/>
        <stop offset="0.45" stop-color="#c79a7e"/>
        <stop offset="1" stop-color="#27303f"/>
      </linearGradient>
      <linearGradient id="collection-band-tone" x1="0" y1="0" x2="0" y2="1">
        <stop offset="0" stop-color="var(--pink)"/>
        <stop offset="1" stop-color="var(--pink-deep)"/>
      </linearGradient>
    </defs>
    <path class="collection-band" fill="url(#collection-band-tone)" d="M0,130 C10,75 75,48 140,50 C210,53 240,115 245,178 C270,150 320,132 370,135 C430,140 473,190 473,250 L473,670 L0,670 Z"/>
    <g role="img" aria-label="Product photo of a skater wearing the first apparel item">
      <use href="#heart" transform="translate(15,160) scale(1.45) rotate(12,50,45)" fill="url(#product-photo-tone)" stroke="var(--white)" stroke-width="5"/>
    </g>
    <g role="img" aria-label="Product photo of a skater wearing the second apparel item">
      <use href="#heart" transform="translate(15,318) scale(1.45) rotate(12,50,45)" fill="url(#product-photo-tone)" stroke="var(--white)" stroke-width="5"/>
    </g>
    <g role="img" aria-label="Product photo of a skater wearing the third apparel item">
      <use href="#heart" transform="translate(15,486) scale(1.45) rotate(12,50,45)" fill="url(#product-photo-tone)" stroke="var(--white)" stroke-width="5"/>
    </g>
  </svg>

  <div class="brand"><span class="brand-dot"></span>Pemby</div>
  <p class="tagline">skatewear for everywhere</p>
  <p class="mission">At Pemby our goal is to provide you cutting edge, super stylish, high quality apparel that’s wearable on the ice or out on the town.</p>

  <h2 class="season-title">Winter</h2>
  <p class="season-sub">Collection</p>

  <div class="product product--one">
    <p class="product-name">Name of apparel</p>
    <p class="product-desc">DESCRIPTION: Lorem Ipsum is simply dummy text of the printing and typesetting industry. Lorem Ipsum has been the industry’s standard dummy text ever since the 1500s,</p>
  </div>
  <div class="price price--one">PRICE : $ 12.34</div>

  <div class="product product--two">
    <p class="product-name">Name of apparel</p>
    <p class="product-desc">DESCRIPTION: Lorem Ipsum is simply dummy text of the printing and typesetting industry. Lorem Ipsum has been the industry’s standard dummy text ever since the 1500s,</p>
  </div>
  <div class="price price--two">PRICE : $ 12.34</div>

  <div class="product product--three">
    <p class="product-name">Name of apparel</p>
    <p class="product-desc">DESCRIPTION: Lorem Ipsum is simply dummy text of the printing and typesetting industry. Lorem Ipsum has been the industry’s standard dummy text ever since the 1500s,</p>
  </div>
  <div class="price price--three">PRICE : $ 12.34</div>

  <p class="contact"><span class="contact-line contact-line--long">Phone: 208-555-0147<span class="sep">|</span>Email: info@pembyskatewear-example.com<span class="sep">|</span>www.pembyskatewear-example.com</span></p>
</section>

</body>
</html>
```